Web Design Project

We are a SaaS company that specializes in the thrift industry POS and inventory software. We want a clean and professional site that does NOT look like a template site.

*** A little more about our business -
We offer a SaaS (Software As A Service) for a Point Of Sale and inventory control product specifically for the Thrift / Second hand industry. The software allows them to process inventory, grade/rate it, create the barcoded tags. It the does the whole retail sale process. We also offer tie-ins to Plumora, Zentiq and pebble/vorn mobile apps to support our customers thrift stores.

We need to in incorporate the look/feel and color scheme of our logo.

I would imagine possibly a HTML5 slideshow (3-5 slides) rotating on the home page showing screenshots, etc.

I am envisioning icons representing features of our product.

PLEASE ask questions, I am sure I have left out a ton.

Reason: I am increasing the budget.

Reason: I have had a harder time with content than I thought I would.

Reason: I was very ill, but I am back and want to get it finished up!

Requirements
Must have
• I have attached a couple of our logo's with color options. It needs to flow with that.

I have also attached a screen shot of what I think might work. This DOESN'T suggest that is what I am looking for, just a sample.

I am thinking a home page and maybe one or two sub pages
***Update, I kind of like the following concept for one of the sub-pages
http://www.quelbrix.example/estimate.html

There should also be a place to highlight Plumora and zentiq.

It will be a bilingual / multilingual site, so take that into account
Should not have
• I don't want it to look like a template site. It should be clean and professional.

```html
<!DOCTYPE html>
<html lang="en">
<head>
<meta charset="utf-8">
<title>resaleright – Home</title>
<link href="https://fonts.googleapis.com/css2?family=Source+Sans+3:ital,wght@0,400;0,600;0,700;1,400&display=swap" rel="stylesheet">
<style>
:root{
  --topbar:#1c252c;
  --header:#29343d;
  --hero-a:#0b93dc;
  --hero-b:#3fb8f2;
  --hero-c:#1aa5ea;
  --strip:rgba(10,110,180,.35);
  --white:#ffffff;
  --ink:#222629;
  --body:#6a6e72;
  --rule:#d7dadd;
  --orange:#f0661c;
  --card-border:#d6d9dc;
  --pill:#e3e5e7;
  --news-a:#e9ebee;
  --news-b:#ffffff;
  --panel:#eceef1;
  --footer:#eef0f2;
  --footer-line:#c9cdd1;
  --brand-blue:#2aa0dc;
}
*{margin:0;padding:0;box-sizing:border-box}
html,body{width:976px;height:1200px;overflow:hidden}
body{position:relative;background:var(--white);font-family:"Source Sans 3",Arial,sans-serif;color:var(--body)}
.abs{position:absolute}

/* top bar & header */
.topbar{left:0;top:0;width:976px;height:20px;background:var(--topbar)}
.topbar-links{right:56px;top:3px;font-size:10px;color:var(--white)}
.topbar-links span{margin:0 3px;color:#8a949b}
.site-header{left:0;top:20px;width:976px;height:83px;background:var(--header)}
.brand{left:32px;top:19px;display:flex;align-items:center;gap:10px}
.brand-square{width:40px;height:40px;background:var(--brand-blue)}
.brand-name{font-size:28px;font-weight:700;color:var(--brand-blue);letter-spacing:-.3px}
.lang-select{left:763px;top:35px;width:162px;height:19px;background:var(--white);border:1px solid #aab;font-size:11px;color:#555;padding:1px 5px}
.lang-select .caret{position:absolute;right:0;top:0;width:17px;height:17px;background:#d7dadd;display:flex;align-items:center;justify-content:center}

/* hero */
.hero{left:0;top:103px;width:976px;height:310px;background:linear-gradient(160deg,var(--hero-a) 0%,var(--hero-b) 55%,var(--hero-c) 100%);overflow:hidden}
.hero-title{left:60px;top:42px;font-size:28px;line-height:31px;color:var(--white);font-weight:400}
.hero-title b{font-weight:700}
.hero-text{left:60px;top:110px;width:415px;font-size:11.2px;line-height:15.5px;color:var(--white)}
.hero-button{left:56px;top:184px;width:152px;height:22px;border:1px solid #9aa;border-radius:11px;background:var(--white);font-size:11px;color:#333;text-align:center;line-height:20px}
.hero-screen{left:636px;top:25px;width:259px;height:212px;border-radius:6px;background:linear-gradient(180deg,#2a2f36 0%,#4a5868 8%,#dfe8f4 10%,#c9d8ec 100%);border:5px solid #1e2227}
.hero-stand{left:740px;top:235px;width:52px;height:30px;background:linear-gradient(180deg,#9aa3ad,#d4d9de)}
.slide-arrow{top:108px}
.service-strip{top:242px;height:68px;background:var(--strip)}
.service-icon{position:absolute;left:18px;top:10px;width:48px;height:48px;border-radius:8px}
.service-title{position:absolute;left:76px;top:7px;font-size:17px;color:var(--white)}
.service-text{position:absolute;left:76px;top:30px;font-size:11px;line-height:13px;color:var(--white)}

/* main */
.section-title{font-size:17.5px;color:var(--ink);font-weight:400}
.section-rule{height:1px;background:linear-gradient(90deg,var(--rule),rgba(215,218,221,0))}
.welcome-text{left:17px;top:478px;width:660px;font-size:11.2px;line-height:16.5px;color:var(--body)}
.welcome-text p{margin-bottom:8px}
.service-card{top:668px;height:240px;border:1px solid var(--card-border);border-radius:8px;background:linear-gradient(180deg,#fff 60%,#f3f4f5);box-shadow:0 6px 8px -4px rgba(0,0,0,.12)}
.card-media{position:absolute;left:11px;top:10px;width:188px;height:104px;border:3px solid #d3d6d9;background:#f4f5f6}
.card-title{position:absolute;left:11px;top:126px;font-size:13px;font-weight:700;color:var(--orange)}
.card-text{position:absolute;left:11px;top:149px;width:192px;font-size:11.2px;line-height:15.5px;color:#4a4e52}
.read-more{position:absolute;right:18px;bottom:16px;height:14px;padding:0 12px;border-radius:7px;background:var(--pill);font-size:10.5px;font-style:italic;line-height:14px;color:#555}

/* sidebar */
.news-item{width:255px;height:98px;background:linear-gradient(180deg,var(--news-a),var(--news-b));padding:8px 14px}
.news-date{font-size:13px;color:var(--ink);margin-bottom:5px}
.news-text{font-size:11.2px;line-height:17px;color:var(--body)}
.pencil{left:890px;top:432px;width:36px;height:40px}
.testimonial{left:711px;top:816px;width:246px;height:128px;border-radius:6px;background:var(--panel);padding:10px 16px}
.testimonial-quote{font-size:11.2px;line-height:17.2px;font-style:italic;color:#555}
.testimonial-author{text-align:right;font-size:11.2px;font-style:italic;color:#222;margin-top:5px}

/* footer */
.site-footer{left:0;top:963px;width:976px;height:189px;background:var(--footer)}
.footer-title{font-size:17.5px;color:var(--ink);font-weight:400}
.footer-links{font-size:11.2px;line-height:19px;color:#444;list-style:none;white-space:nowrap}
.footer-divider{width:1px;height:136px;background:var(--footer-line)}
.bullet-list li{padding-left:10px;position:relative;margin-bottom:0;background:linear-gradient(90deg,#fff 70%,rgba(255,255,255,0));width:130px}
.bullet-list li::before{content:"";position:absolute;left:1px;top:8px;width:4px;height:4px;background:#333}
.social-squares{left:710px;top:44px;display:flex;gap:4px}
.social-squares i{display:block;width:23px;height:23px;border-radius:3px}
.social-names{left:712px;top:80px;font-size:11.2px;color:#444}
.social-names span{margin:0 4px;color:#888}
.bottom-bar{left:0;top:1152px;width:976px;height:48px;background:var(--header);color:var(--white);font-size:11.2px}
.bottom-bar span{color:#8a949b;margin:0 4px}
</style>
</head>
<body>

<div class="abs topbar">
  <div class="abs topbar-links">Login<span>|</span>Register<span>|</span>Sitemap</div>
</div>

<header class="abs site-header">
  <div class="abs brand"><div class="brand-square"></div><div class="brand-name">resaleright</div></div>
  <div class="abs lang-select">Select Your Language<span class="caret"><svg width="8" height="5"><path d="M0 0h8L4 5z" fill="#555"/></svg></span></div>
</header>

<section class="abs hero">
  <svg class="abs" style="left:0;top:0" width="976" height="310">
    <path d="M480 90 C600 40 760 160 976 60" stroke="rgba(255,255,255,.18)" fill="none" stroke-width="1.5"/>
    <path d="M480 120 C620 60 780 190 976 100" stroke="rgba(255,255,255,.14)" fill="none" stroke-width="1.5"/>
    <path d="M480 150 C640 90 800 220 976 140" stroke="rgba(255,255,255,.1)" fill="none" stroke-width="1.5"/>
  </svg>
  <svg class="abs slide-arrow" style="left:10px" width="28" height="78"><path d="M26 2 L2 39 L26 76" stroke="rgba(255,255,255,.7)" stroke-width="1.5" fill="none"/></svg>
  <svg class="abs slide-arrow" style="left:934px" width="28" height="78"><path d="M2 2 L26 39 L2 76" stroke="rgba(255,255,255,.7)" stroke-width="1.5" fill="none"/></svg>

  <h1 class="abs hero-title"><b>Resale Right</b> Punch Line<br>Goes here !</h1>
  <p class="abs hero-text">Brightwave Studio is a web service company, offering a wide range of services which range from designing and development, that is covering almost all the fields in the best possible way. To be the best we know what and how to present beautifully the working of the client's need and their advantages be highlighted.</p>
  <div class="abs hero-button">CLICK HERE TO READ MORE</div>

  <div class="abs hero-screen" role="img" aria-label="Desktop monitor showing the point of sale dashboard screenshot"></div>
  <div class="abs hero-stand" role="img" aria-label="Monitor stand"></div>

  <div class="abs service-strip" style="left:7px;width:232px">
    <div class="service-icon" style="background:radial-gradient(circle at 40% 40%,#e8f4fc,#4c8fc8)" role="img" aria-label="Globe and gear icon"></div>
    <div class="service-title">1st Services Point</div>
    <div class="service-text">Need and their advantages<br>be highlighted.</div>
  </div>
  <div class="abs service-strip" style="left:241px;width:217px">
    <div class="service-icon" style="left:14px;background:linear-gradient(180deg,#9fe0fb,#2e7fb5)" role="img" aria-label="Monitor icon"></div>
    <div class="service-title" style="left:70px">IInd Services Point</div>
    <div class="service-text" style="left:70px">Need and their advantages<br>be highlighted.</div>
  </div>
  <div class="abs service-strip" style="left:460px;width:216px">
    <div class="service-icon" style="left:12px;background:linear-gradient(135deg,#f4d36a,#e7eaee)" role="img" aria-label="Document with magnifying glass icon"></div>
    <div class="service-title" style="left:77px">IIIrd Services</div>
    <div class="service-text" style="left:77px">Need and their advantages<br>be highlighted.</div>
  </div>
</section>

<main>
  <h2 class="abs section-title" style="left:17px;top:446px">Welcome to Our Website Mainpage..</h2>
  <div class="abs section-rule" style="left:17px;top:469px;width:630px"></div>
  <div class="abs welcome-text">
    <p>Brightwave Studio is a professional website design company dedicated to provide excellent services. We at Brightwave Studio think graphic design as a combination and collaboration of ideas and technology. Our Website Design team give an unforgettable impression on the customers and the clients. We can assure you that this is the best place for requirement of yours regarding website design solutions</p>
    <p>Brightwave Studio provides you the Search Engine Optimization making your website search engine friendly. So that the website can achieve top position and ranking in the Internet searches and thereby increasing the scope for the website to be found by customers. We here modify the site to improve the ranking by using the keywords and contents.</p>
  </div>

  <h2 class="abs section-title" style="left:16px;top:630px">Featured Services</h2>
  <div class="abs section-rule" style="left:16px;top:654px;width:630px"></div>

  <article class="abs service-card" style="left:16px;width:216px">
    <div class="card-media" style="background:linear-gradient(180deg,#f7f8f9,#d4e7f5)" role="img" aria-label="Sales report bar chart screenshot"></div>
    <h3 class="card-title">SERVICES GOES HERE</h3>
    <p class="card-text">We can assure you that this is the best place for requirement of yours regard-ing website design solutions</p>
    <span class="read-more">read more here..</span>
  </article>

  <article class="abs service-card" style="left:239px;width:217px">
    <div class="card-media" style="background:linear-gradient(135deg,#2a2d31,#5a6068 60%,#d9dde1)" role="img" aria-label="Tablet displaying an inventory report"></div>
    <h3 class="card-title">SERVICES GOES HERE</h3>
    <p class="card-text">We can assure you that this is the best place for requirement of yours regard-ing website design solutions</p>
    <span class="read-more">read more here..</span>
  </article>

  <article class="abs service-card" style="left:462px;width:216px">
    <div class="card-media" style="background:linear-gradient(135deg,#a5774f,#d9b89a 45%,#eef0f2)" role="img" aria-label="Hands holding a printed sales receipt"></div>
    <h3 class="card-title">SERVICES GOES HERE</h3>
    <p class="card-text">We can assure you that this is the best place for requirement of yours regard-ing website design solutions</p>
    <span class="read-more">read more here..</span>
  </article>
</main>

<aside>
  <h2 class="abs section-title" style="left:707px;top:450px">Recent News &amp; Updates</h2>
  <div class="abs pencil" style="background:linear-gradient(135deg,#f6c343,#e29a1f)" role="img" aria-label="Pencil icon"></div>

  <div class="abs news-item" style="left:703px;top:482px">
    <div class="news-date">20.Jan.2012</div>
    <p class="news-text">Brightwave Studio is a professional website design company dedicated to provide excellent services.</p>
  </div>
  <div class="abs news-item" style="left:706px;top:581px">
    <div class="news-date">20.Jan.2012</div>
    <p class="news-text">Brightwave Studio is a professional website design company dedicated to provide excellent services.</p>
  </div>
  <div class="abs news-item" style="left:710px;top:674px">
    <div class="news-date">20.Jan.2012</div>
    <p class="news-text">Brightwave Studio is a professional website design company dedicated to provide excellent services.</p>
  </div>

  <h2 class="abs section-title" style="left:719px;top:787px">Testimonials</h2>
  <div class="abs testimonial">
    <p class="testimonial-quote">Engine Optimization making your website search engine friendly. So that the website can achieve top position and ranking in the Internet searches and thereby increasing the scope for the website to be found by custom-</p>
    <p class="testimonial-author">By Author Name</p>
  </div>
</aside>

<footer class="abs site-footer">
  <h3 class="abs footer-title" style="left:20px;top:13px">Company</h3>
  <ul class="abs footer-links" style="left:21px;top:44px">
    <li>Main page</li><li>Services Overview</li><li>About Company</li><li>Testimonials</li><li>Partners</li>
  </ul>
  <ul class="abs footer-links" style="left:145px;top:44px">
    <li>Member Log In</li><li>Recent Blog</li><li>Support &amp; FAQ</li><li>Contact Us</li>
  </ul>
  <div class="abs footer-divider" style="left:247px;top:5px"></div>

  <h3 class="abs footer-title" style="left:287px;top:13px">Services List</h3>
  <ul class="abs footer-links bullet-list" style="left:287px;top:44px">
    <li>Your Services goes here</li><li>Services goes here</li><li>Your Services goes</li><li>Your Services goes here</li>
  </ul>
  <ul class="abs footer-links bullet-list" style="left:449px;top:44px">
    <li>Your Services goes here</li><li>Services goes here</li><li>Your Services goes</li><li>Your Services goes here</li>
  </ul>
  <div class="abs footer-divider" style="left:619px;top:5px"></div>

  <h3 class="abs footer-title" style="left:710px;top:14px">Connect With Us</h3>
  <div class="abs social-squares">
    <i style="background:#2a78b4"></i><i style="background:#3b5a9a"></i><i style="background:#35a6d8"></i><i style="background:#c9302c"></i>
  </div>
  <div class="abs social-names">Netlinq<span>|</span>Plumora<span>|</span>Zentiq<span>|</span>Vidova</div>
</footer>

<div class="abs bottom-bar">
  <div class="abs" style="left:27px;top:17px">Privacy Policy<span>|</span>Terms &amp; Conditions</div>
  <div class="abs" style="left:668px;top:15px">Copyright © 2012 Company Name<span>|</span>All right reserved</div>
</div>

</body>
</html>
```